We need a business card design for an assisted living facility in Los Angeles. We have a logo selected but we would like a business card design that will leave a lasting impression on families looking to place their elderly loved ones in our care as well as on other facility providers who may refer their elderly residents to our facility.

```html
<!DOCTYPE html>
<html lang="en">
<head>
<meta charset="utf-8">
<title>Harborview Grace Senior Living — Business Card</title>
<link rel="stylesheet" href="https://fonts.googleapis.com/css2?family=Open+Sans:wght@400;600;700&display=swap">
<style>
  :root {
    --stage: #222222;
    --card-dark: #1b1b1c;
    --brand-blue: #127dc4;
    --band-gray: #8a8a8c;
    --text-light: #f2f2f2;
    --text-muted: #8e8e90;
  }
  * { box-sizing: border-box; margin: 0; padding: 0; }
  html, body {
    width: 1200px; height: 780px; overflow: hidden;
    background: var(--stage);
    font-family: "Open Sans", sans-serif;
  }
  .stage { position: relative; width: 1200px; height: 780px; }
  .card {
    position: absolute; top: 241px;
    width: 520px; height: 298px; overflow: hidden;
  }
  .card--info { left: 60px; background: var(--card-dark); }
  .card--brand { left: 620px; background: var(--brand-blue); }

  .card__bands { position: absolute; inset: 0; }

  .wordmark {
    position: absolute; text-transform: uppercase;
    font-weight: 400; letter-spacing: 0.08em; line-height: 1.25;
    text-align: center;
  }
  .card--info .wordmark {
    left: 26px; top: 108px; width: 210px;
    font-size: 16px; color: var(--brand-blue);
  }
  .card--brand .wordmark {
    left: 0; right: 0; top: 118px;
    font-size: 24px; color: #ffffff;
  }

  .contact {
    position: absolute; left: 282px; top: 70px;
    color: var(--text-light); font-size: 12.5px; line-height: 1.45;
  }
  .contact__name { font-size: 21px; font-weight: 700; line-height: 1.2; }
  .contact__first { color: var(--text-muted); }
  .contact__last { color: var(--brand-blue); }
  .contact__role { font-weight: 600; margin-bottom: 8px; }
  .contact__address { margin-bottom: 6px; }
  .contact__line { display: flex; align-items: center; gap: 6px; }
  .contact__icon { width: 11px; height: 11px; flex: none; }
</style>
</head>
<body>
<main class="stage">

  <section class="card card--info" aria-label="Business card, contact side">
    <svg class="card__bands" width="520" height="298" viewBox="0 0 520 298" aria-hidden="true">
      <defs>
        <linearGradient id="divider-fade" x1="0" y1="1" x2="0" y2="0">
          <stop offset="0" stop-color="#ffffff" stop-opacity="0"/>
          <stop offset="0.5" stop-color="#ffffff" stop-opacity="0.9"/>
          <stop offset="1" stop-color="#ffffff" stop-opacity="0"/>
        </linearGradient>
      </defs>
      <polygon points="0,0 292,0 276,16 0,16" fill="var(--brand-blue)"/>
      <polygon points="188,288 520,288 520,298 180,298" fill="var(--band-gray)"/>
      <line x1="240" y1="262" x2="268" y2="48" stroke="url(#divider-fade)" stroke-width="1.4"/>
    </svg>

    <p class="wordmark">Harborview Grace<br>Senior Living</p>

    <div class="contact">
      <p class="contact__name"><span class="contact__first">Marina</span> <span class="contact__last">Lindqvist</span></p>
      <p class="contact__role">Managing Director</p>
      <p class="contact__address">1840 Cedar Hollow Rd. Suite 300<br>Pasadena, CA 91105</p>
      <p class="contact__line">
        <svg class="contact__icon" viewBox="0 0 12 12" aria-hidden="true"><path d="M2.4 1 4 1 5 3.6 3.8 4.6C4.4 6 5.9 7.6 7.4 8.2L8.4 7 11 8 11 9.6C11 10.4 10.3 11 9.5 11 5 10.6 1.4 7 1 2.5 1 1.7 1.6 1 2.4 1Z" fill="var(--brand-blue)"/></svg>
        (626) 555-0148
      </p>
      <p class="contact__line">
        <svg class="contact__icon" viewBox="0 0 12 12" aria-hidden="true"><rect x="0.5" y="2" width="11" height="8" rx="1" fill="var(--brand-blue)"/><path d="M1 2.6 6 6.6 11 2.6" fill="none" stroke="var(--card-dark)" stroke-width="1"/></svg>
        info@harborviewgrace.com
      </p>
      <p class="contact__line">
        <svg class="contact__icon" viewBox="0 0 12 12" aria-hidden="true"><circle cx="6" cy="6" r="5.3" fill="var(--brand-blue)"/><path d="M0.8 6H11.2M6 0.8C3.8 3.5 3.8 8.5 6 11.2M6 0.8C8.2 3.5 8.2 8.5 6 11.2" fill="none" stroke="var(--card-dark)" stroke-width="0.8"/></svg>
        www.harborviewgrace.com
      </p>
    </div>
  </section>

  <section class="card card--brand" aria-label="Business card, brand side">
    <p class="wordmark">Harborview Grace<br>Senior Living</p>
  </section>

</main>
</body>
</html>
```